Consulting company business cards

We have a base design, but would be willing to update. We have a new logo/"tag" that needs to be added. Current business card design is attached for reference into our "style."

Industry/Entity Type

Business

Contact Information for Business Card

Should contain name and title, office number, mobile number if appropriate, e-mail, website, physical address, and company logo.

Font styles to use
Other font styles liked:
• See current card design on DrovankBCard

Colors
0455a3
85acd3
aaaaaa

Requirements
Must have
• Our colors are navy blue, gray, and a lighter blue
Nice to have
• Design that I can easily drop in new names/titles as we hire employees.

```html
<!DOCTYPE html>
<html lang="en">
<head>
<meta charset="utf-8">
<title>Tessaro Business Cards</title>
<link rel="stylesheet" href="https://fonts.googleapis.com/css2?family=Lato:wght@400;700;900&display=swap">
<style>
  :root {
    --backdrop: #d6d6d6;
    --card: #f1f1f1;
    --card-lower: #ebebeb;
    --navy: #0b2a45;
    --rule: #141c28;
    --blue: #1f86c6;
    --charcoal: #25272b;
    --gray: #8f8f8f;
    --ink: #1e1e1e;
    --white: #ffffff;
  }
  * { box-sizing: border-box; margin: 0; padding: 0; }
  html, body { width: 1200px; height: 900px; overflow: hidden; }
  body {
    background: var(--backdrop);
    font-family: "Lato", Arial, sans-serif;
    position: relative;
  }
  .card {
    position: absolute;
    width: 525px;
    height: 300px;
    background: var(--card);
    box-shadow: 0 2px 6px rgba(0,0,0,0.18);
    overflow: hidden;
  }
  .card--front { left: 80px; top: 80px; }
  .card--back { left: 595px; top: 520px; }

  .front__lower {
    position: absolute; left: 0; right: 0; top: 150px; bottom: 0;
    background: var(--card-lower);
    border-top: 3px solid var(--rule);
  }

  .lockup { position: absolute; }
  .lockup__row { display: flex; align-items: center; gap: 12px; }
  .lockup__name {
    font-weight: 700;
    color: var(--navy);
    letter-spacing: 0.5px;
    line-height: 1;
  }
  .lockup__mark {
    width: 14px; height: 14px;
    background: var(--blue);
  }
  .lockup__tagline {
    color: var(--gray);
    letter-spacing: 0.8px;
    font-weight: 400;
    margin-top: 6px;
  }
  .card--front .lockup { left: 165px; top: 58px; }
  .card--front .lockup__name { font-size: 46px; }
  .card--front .lockup__tagline { font-size: 13px; }

  .back__person { position: absolute; left: 40px; top: 30px; }
  .person__name { font-size: 26px; color: var(--ink); font-weight: 400; letter-spacing: 0.5px; }
  .person__name b { font-weight: 900; }
  .person__title { font-size: 19px; color: var(--blue); letter-spacing: 1px; }

  .back__panel {
    position: absolute; left: 0; top: 112px; width: 285px; bottom: 0;
    background: var(--charcoal);
    color: var(--white);
    padding: 24px 60px 0 50px;
    font-size: 13px;
    line-height: 1.35;
  }
  .contact-group { padding: 6px 0 7px; border-bottom: 1px solid #3c3f44; }
  .contact-group:last-child { border-bottom: none; }

  .back__rule {
    position: absolute; left: 285px; right: 0; top: 136px;
    border-top: 3px solid var(--rule);
  }
  .back__icons {
    position: absolute; left: 255px; top: 150px; width: 44px; height: 145px;
    background: var(--blue);
    display: flex; flex-direction: column; justify-content: space-around; align-items: center;
    box-shadow: 2px 0 4px rgba(0,0,0,0.25);
  }
  .back__icons svg { width: 20px; height: 20px; }

  .card--back .lockup { left: 335px; top: 198px; }
  .card--back .lockup__name { font-size: 36px; }
  .card--back .lockup__mark { width: 11px; height: 11px; }
  .card--back .lockup__tagline { font-size: 10px; }
</style>
</head>
<body>

<section class="card card--front" aria-label="Card front">
  <div class="front__lower"></div>
  <div class="lockup">
    <div class="lockup__row">
      <span class="lockup__mark"></span>
      <span class="lockup__name">Tessaro</span>
    </div>
    <div class="lockup__tagline">Cloud Strategy &amp; Advisory</div>
  </div>
</section>

<section class="card card--back" aria-label="Card back">
  <div class="back__person">
    <div class="person__name"><b>ALEX</b> MORENO</div>
    <div class="person__title">FOUNDER</div>
  </div>

  <div class="back__panel">
    <div class="contact-group">Address Line 1<br>Address Line 2<br>Address Line 3</div>
    <div class="contact-group">Phone: 123 456 789<br>Fax: 123 456 789</div>
    <div class="contact-group">alex@email.com<br>www.website.com</div>
  </div>

  <div class="back__rule"></div>

  <div class="back__icons">
    <svg viewBox="0 0 20 20" aria-label="Address">
      <path d="M2 10 L10 3 L18 10" fill="none" stroke="#fff" stroke-width="2"/>
      <rect x="5" y="9" width="10" height="8" fill="#fff"/>
      <rect x="9" y="12" width="2.5" height="5" fill="#1f86c6"/>
    </svg>
    <svg viewBox="0 0 20 20" aria-label="Phone">
      <path d="M3 7 Q10 2 17 7 L15 9 L13 7.5 L7 7.5 L5 9 Z" fill="#fff"/>
      <rect x="5" y="10" width="10" height="7" rx="1.5" fill="#fff"/>
      <circle cx="10" cy="13.5" r="1.8" fill="#1f86c6"/>
    </svg>
    <svg viewBox="0 0 20 20" aria-label="Website">
      <rect x="2" y="3" width="16" height="11" fill="none" stroke="#fff" stroke-width="1.8"/>
      <rect x="8" y="14" width="4" height="3" fill="#fff"/>
      <rect x="5" y="17" width="10" height="1.6" fill="#fff"/>
    </svg>
  </div>

  <div class="lockup">
    <div class="lockup__row">
      <span class="lockup__mark"></span>
      <span class="lockup__name">Tessaro</span>
    </div>
    <div class="lockup__tagline">Cloud Strategy &amp; Advisory</div>
  </div>
</section>

</body>
</html>
```